E-Book-Cover für meinen Roman Was der Nebel trägt
Sehr angenehmer Kontakt, das Beschriebene wurde auf Anhieb in die Richtung umgesetzt, die ich angestrebt habe. Änderungswünsche wurden prompt und unermüdlich umgesetzt, bis das Endergebnis stand. Sehr zu empfehlen!
Zielgruppe
Ich veröffentliche in Eigenregie meinen Roman namens 'Was der Nebel trägt' im Rahmen des Self-Publishing Angebots von Lesowa.de
Bei meinem Werk handelt es sich um Belletristik: eine Geschichte aus dem Leben, die traurige und lustige Elemente zu gleichen Teilen eint. Behandelt wird der Lebensabschnitt eines Jugendlichen, der zu früh Erfahrung mit dem Tod macht, als seine Mutter schwer erkrankt. Gleichzeitig gilt es, den (humorvoll verpackten) Alltag zu meistern, in dem er wieder und wieder auf Ablehnung und Distanz angesichts seiner ungewöhnlichen und misslichen Lage stößt. Es gelingt ihm nicht mehr, Teil seiner gleichaltrigen Mitstreiter zu werden.
Gleichzeitig gibt es einen zweiten Handlungsstrang, in dem eine ebenfalls Jugendliche ähnliche Erfahrungen macht, auch wenn die Umstände andere sind, ebenso wie die Reaktion darauf. Während der männliche Protagonist wiederholt von seinem Umkreis enttäuscht wird, stellt er sich am Ende der Prüfung, der er nicht entkommen kann. Sein weibliches Pendant hingegen tritt eine überstürzte Flucht mit ungewissem Ausgang an. Beide Stränge sind lose miteinander verwoben, und als Leser stellt man sich zusehends die Frage, ob und wann diese verbunden werden. Eine Auflösung erfolgt am Schluss.
Nach einigen Testlesern stellte sich heraus, dass jene am meisten begeistert waren, die selbst ähnliche Erfahrungen gemacht haben, wie die fiktiven Personen. Grundsätzlich lässt sich aber sagen, dass der Schreibstil, die beschriebenen Medien und Situationen eher auf (junge) Erwachsene zugeschnitten sind. Dennoch handelt es sich nicht um ein klassisches Jugendbuch, oft werden Dinge beschrieben, die für Minderjährige nicht geeignet sind. Als (Haupt)zielgruppe würde ich grob den Rahmen 20-40 Jahre vorgeben, wobei die Leser eher noch älter als jünger sein dürfen.
Aufgabenstellung
Zunächst technisch: (Angaben lt. Lesowa)
JPEG oder TIFF-Datei
mindestens 1000 Pixel an der längsten Seite
Idealverhältnis von Bildhöhe- und breite: 1,6 (Beispiel: 1000 x 1600)
bei weißen Covern sollte ein 2-3 Pixel breiter, grauer Rand hinzugefügt werden, damit sich das Cover von der Website selbst abhebt
Weiterhin zu beachten:
-Hauptsächlich wird es auf eBook Readern gelesen, die nur in Graustufen darstellen. Das Cover sollte also in jedem Fall auch in Schwarz-Weiß nichts von seiner Wirkung einbüßen!
Selbiges gilt für eine Miniaturansicht!
Autor: Matthias Krollner
Titel: Was der Nebel trägt
Zusatz: Roman
Nun zu den wichtigsten Vorgaben:
-Selbstverständlich soll das Cover Aufmerksamkeit erzeugen und neugierig machen.
-Das Thema "anders sein" / "im Abseits stehen" / "hin- und hergetrieben werden" muss auf jeden Fall rübergebracht werden, da dies auch das Kernthema des Buches ist.
-Bei der Schriftart gibt es keine bestimmte Vorgabe, nur bitte nichts in Kapitälchen oder Großbuchstaben. (z.B. WAS DER NEBEL TRÄGT)
-Es soll auf keinen Fall übertrieben ernst oder möchtegern-schnulzig rüberkommen. (Bilder vom Strand, untergehender Sonne und weitere Klischees.)
-Vielmehr darf man dem Cover bereits ansehen, dass es ein ernstes Thema auch mit Humor nehmen kann. z.B. durch Stilisierung, einfache Farben anstatt aufwändiger Realaufnahmen und Schatten, evtl. auch in Richtung Comic, aber nicht zu albern.
-Die Platzierung von Autor und Titel darf klassisch sein, gerne aber auch ungewöhnlich überraschend.
Ich habe diesem Inserat einige Entwürfe meinerseits beigefügt, wie ich das o.g. Thema stilisieren würde, z.B.:
der Querschnitt eines einfahrenden Zuges (Hauptverkehrsmittel im Buch), bei dem in allen Fenstern Licht brennt, mit Ausnahme von einem. (Hier dürfen gerne auch die Profile von Menschen hinzug..

```html
<!DOCTYPE html>
<html lang="de">
<head>
<meta charset="utf-8">
<title>Was der Nebel trägt – Roman – Matthias Krollner</title>
<link rel="stylesheet" href="https://fonts.googleapis.com/css2?family=Source+Serif+4:opsz,wght@8..60,400;8..60,500;8..60,600&display=swap">
<style>
  :root {
    --page: #ffffff;
    --frame: #d9d9d9;
    --title-orange: #ee8f22;
    --title-red: #b81e2b;
    --title-coral: #e4512a;
    --label-grey: #5c5c5c;
    --author-ink: #333333;
    --sky-pale: #f8c690;
    --sky-gold: #f6b82a;
    --sky-deep: #f0964a;
    --ground-coral: #e8775a;
  }
  html, body {
    margin: 0;
    padding: 0;
    width: 877px;
    height: 1200px;
    overflow: hidden;
    background: var(--page);
  }
  .cover {
    position: relative;
    width: 877px;
    height: 1200px;
    background: var(--page);
    font-family: "Source Serif 4", Georgia, serif;
  }
  .cover-frame {
    position: absolute;
    left: 131px;
    top: 106px;
    width: 615px;
    height: 985px;
    box-sizing: border-box;
    border: 7px solid var(--frame);
    background: var(--page);
  }
  .scene-illustration {
    position: absolute;
    left: 138px;
    top: 113px;
    width: 601px;
    height: 590px;
    display: block;
  }
  .title-line {
    position: absolute;
    left: 138px;
    width: 601px;
    margin: 0;
    text-align: center;
    line-height: 1;
    font-weight: 600;
    white-space: nowrap;
  }
  .title-line--first {
    top: 651px;
    font-size: 84px;
    color: var(--title-orange);
    font-weight: 500;
  }
  .title-line--main {
    top: 706px;
    font-size: 140px;
    color: var(--title-red);
    letter-spacing: -1px;
  }
  .title-line--last {
    top: 834px;
    font-size: 84px;
    color: var(--title-coral);
  }
  .genre-label {
    position: absolute;
    left: 138px;
    width: 601px;
    top: 930px;
    margin: 0;
    text-align: center;
    font-size: 20px;
    line-height: 1;
    color: var(--label-grey);
    font-weight: 400;
  }
  .author-name {
    position: absolute;
    left: 138px;
    width: 601px;
    top: 992px;
    margin: 0;
    text-align: center;
    font-size: 34px;
    line-height: 1;
    color: var(--author-ink);
    font-weight: 500;
  }
</style>
</head>
<body>
  <main class="cover">
    <div class="cover-frame"></div>

    <svg class="scene-illustration" viewBox="0 0 601 590" role="img"
         aria-label="Stilisierte Zeichnung: Bahngleise mit Oberleitungen laufen in die Ferne, ein sitzender Junge zwischen den Schienen, dahinter ein orangefarbener Himmel">
      <defs>
        <linearGradient id="sky-band" x1="0" y1="0" x2="1" y2="0">
          <stop offset="0" stop-color="var(--sky-pale)"/>
          <stop offset="0.6" stop-color="var(--sky-gold)"/>
          <stop offset="1" stop-color="var(--sky-deep)"/>
        </linearGradient>
        <linearGradient id="scene-fade" x1="0" y1="0" x2="0" y2="1">
          <stop offset="0" stop-color="#ffffff" stop-opacity="1"/>
          <stop offset="0.18" stop-color="#ffffff" stop-opacity="0"/>
          <stop offset="0.45" stop-color="#ffffff" stop-opacity="0"/>
          <stop offset="0.5" stop-color="#222222" stop-opacity="0.85"/>
          <stop offset="0.56" stop-color="var(--ground-coral)" stop-opacity="1"/>
          <stop offset="0.72" stop-color="#ffffff" stop-opacity="0.9"/>
          <stop offset="1" stop-color="#ffffff" stop-opacity="1"/>
        </linearGradient>
      </defs>
      <rect x="0" y="0" width="601" height="590" fill="url(#sky-band)"/>
      <rect x="0" y="0" width="601" height="590" fill="url(#scene-fade)"/>
    </svg>

    <h1 class="book-title">
      <span class="title-line title-line--first">Was der</span>
      <span class="title-line title-line--main">Nebel</span>
      <span class="title-line title-line--last">trägt</span>
    </h1>
    <p class="genre-label">Roman</p>
    <p class="author-name">Matthias Krollner</p>
  </main>
</body>
</html>
```